Crowdfunding a casino! Lotrafy.io

looking for an attractive flashy design that sells a casino idea that needs crowdfunding. need a custom logo int he design as well that's why we offer a high price :)

```html
<!DOCTYPE html>
<html lang="en">
<head>
<meta charset="utf-8">
<title>Lotrafy — Crowdfunding the MetaVerse Casino</title>
<link href="https://fonts.googleapis.com/css2?family=Oswald:wght@400;500;700&family=Barlow:wght@400;500;600;700&display=swap" rel="stylesheet">
<style>
  :root {
    --violet-deep: #12021a;
    --violet-dark: #1d0529;
    --violet: #3a0a52;
    --violet-bright: #6a1a8c;
    --crimson: #ff1f5a;
    --crimson-dark: #c4103f;
    --white: #ffffff;
    --text-soft: #e9ddf0;
    --card-text: #4a4050;
    --footer-bg: #0d0110;
    --gold: #f0a94a;
  }
  * { box-sizing: border-box; margin: 0; padding: 0; }
  a { text-decoration: none; }
  html, body { width: 1200px; height: 3306px; overflow: hidden; }
  body {
    position: relative;
    background: var(--violet-deep);
    font-family: "Barlow", Arial, sans-serif;
    color: var(--white);
  }
  .section { position: absolute; left: 0; width: 1200px; overflow: hidden; }
  .heading {
    font-family: "Oswald", Impact, sans-serif;
    font-weight: 700;
    text-transform: uppercase;
    color: var(--white);
    text-shadow: 2px 2px 0 var(--crimson), 0 0 14px rgba(255,31,90,.45);
    letter-spacing: .5px;
  }
  .btn {
    position: absolute;
    display: flex; align-items: center; justify-content: center;
    background: var(--white);
    color: var(--crimson);
    font-family: "Oswald", Impact, sans-serif;
    font-weight: 500;
    text-transform: uppercase;
    text-decoration: none;
    border: 2px solid var(--crimson);
    box-shadow: 5px 5px 0 var(--crimson-dark);
  }
  .brand {
    font-family: "Barlow", Arial, sans-serif;
    font-weight: 600;
    color: var(--white);
    text-transform: uppercase;
    display: flex; align-items: center;
  }
  .brand-dot { border-radius: 50%; background: var(--crimson); margin-right: 12px; }

  /* Hero */
  .hero {
    top: 0; height: 598px;
    background: radial-gradient(ellipse at 70% 40%, #7a2a9c 0%, #561478 45%, #3b0a55 100%);
  }
  .hero .brand { position: absolute; left: 62px; top: 38px; font-size: 32px; }
  .hero .brand-dot { width: 26px; height: 26px; }
  .main-nav { position: absolute; top: 48px; left: 0; }
  .main-nav a {
    position: absolute; white-space: nowrap;
    font-family: "Oswald", sans-serif; font-size: 17px; color: var(--white);
    text-transform: uppercase;
  }
  .hero-title { position: absolute; left: 110px; top: 182px; font-size: 60px; line-height: 1.1; }
  .hero-sub { position: absolute; left: 110px; top: 272px; width: 560px; font-size: 25px; line-height: 36px; color: var(--text-soft); }
  .hero .btn { left: 110px; top: 384px; width: 176px; height: 55px; font-size: 19px; }
  .hero-art {
    position: absolute; left: 757px; top: 0; width: 443px; height: 598px;
    background: radial-gradient(circle at 85% 60%, #2a1a3c 0%, #5a1f62 40%, rgba(90,20,120,0) 75%);
  }

  /* Why */
  .why {
    top: 598px; height: 464px;
    background: linear-gradient(180deg, #1a0322 0%, #12021a 100%);
  }
  .why-art {
    position: absolute; left: 103px; top: 56px; width: 436px; height: 360px;
    background: radial-gradient(ellipse at 50% 55%, #a9561a 0%, #4a1c1c 40%, rgba(18,2,26,0) 72%);
  }
  .why-title { position: absolute; left: 599px; top: 88px; font-size: 42px; }
  .why-text {
    position: absolute; left: 602px; top: 164px; width: 486px;
    font-size: 17px; line-height: 30px; color: var(--text-soft); text-align: justify;
  }

  /* How it works */
  .how {
    top: 1062px; height: 901px;
    background: linear-gradient(180deg, #12021a 0%, #1d0529 55%, #3a0a52 100%);
  }
  .how-title { position: absolute; left: 0; width: 1200px; top: 82px; text-align: center; font-size: 42px; }
  .how-text {
    position: absolute; left: 128px; top: 198px; width: 950px;
    font-size: 17px; line-height: 33.4px; color: var(--text-soft); text-align: center;
  }
  .round-card {
    position: absolute; top: 537px; width: 313px; height: 236px;
    background: var(--white); border-radius: 4px;
    box-shadow: 0 6px 0 rgba(120,60,140,.5);
  }
  .round-card.first { border: 2px solid #f2a04a; }
  .round-badge {
    position: absolute; left: 105px; top: -52px; width: 104px; height: 104px;
    border-radius: 50%; background: var(--violet);
    border: 3px solid var(--crimson);
    display: flex; align-items: center; justify-content: center;
    font-family: "Oswald", sans-serif; color: var(--white);
  }
  .round-badge .label { font-size: 21px; font-weight: 500; }
  .round-badge .num { font-size: 54px; font-weight: 700; color: var(--violet); -webkit-text-stroke: 2px var(--crimson); margin-left: 4px; line-height: 1; }
  .round-text {
    position: absolute; left: 28px; top: 90px; width: 257px;
    font-size: 16.5px; line-height: 27px; color: var(--card-text); text-align: center;
  }
  .round-card .btn { left: 66px; top: 201px; width: 177px; height: 56px; font-size: 19px; }

  /* Human touch */
  .human {
    top: 1963px; height: 652px;
    background: linear-gradient(90deg, #1d0529 0%, #241033 60%, #2a1a3e 100%);
  }
  .human-art {
    position: absolute; left: 539px; top: 10px; width: 661px; height: 642px;
    background: radial-gradient(ellipse at 45% 55%, #8a5a2a 0%, #3a2840 40%, rgba(36,16,51,0) 75%);
  }
  .human-title { position: absolute; left: 113px; top: 94px; font-size: 42px; }
  .feature { position: absolute; left: 113px; width: 450px; }
  .feature h3 {
    display: flex; align-items: center;
    font-family: "Barlow", sans-serif; font-weight: 700; font-size: 19px;
    color: var(--crimson); text-transform: uppercase;
  }
  .feature h3 svg { margin-right: 10px; }
  .feature p { margin-top: 8px; font-size: 17px; line-height: 30px; color: var(--text-soft); }

  /* Future */
  .future {
    top: 2615px; height: 394px;
    background: linear-gradient(180deg, #1d0529 0%, #2e0842 60%, #3a0a52 100%);
  }
  .future-title { position: absolute; left: 0; width: 1200px; top: 90px; text-align: center; font-size: 42px; }
  .future-text {
    position: absolute; left: 250px; top: 165px; width: 700px;
    font-size: 17px; line-height: 30px; color: var(--text-soft); text-align: center;
  }

  /* Footer */
  .footer { top: 3009px; height: 297px; background: var(--footer-bg); }
  .footer .brand { position: absolute; left: 112px; top: 58px; font-size: 54px; }
  .footer .brand-dot { width: 40px; height: 40px; }
  .socials { position: absolute; top: 72px; left: 862px; display: flex; gap: 26px; }
  .socials span { width: 16px; height: 16px; border-radius: 50%; background: var(--crimson); }
  .newsletter-label {
    position: absolute; left: 645px; top: 120px;
    font-family: "Oswald", sans-serif; font-size: 15px; text-transform: uppercase;
  }
  .email-field {
    position: absolute; left: 645px; top: 149px; width: 257px; height: 45px;
    background: #f2f2f2; color: #777; font-size: 15px; padding-left: 28px;
    display: flex; align-items: center;
  }
  .subscribe-btn {
    position: absolute; left: 906px; top: 149px; width: 183px; height: 45px;
    background: var(--crimson); color: var(--white); font-size: 17px; font-weight: 600;
    display: flex; align-items: center; justify-content: center;
  }
  .footer-nav a {
    position: absolute; top: 176px; white-space: nowrap;
    font-family: "Oswald", sans-serif; font-size: 17px; color: var(--white);
    text-transform: uppercase;
  }
  .footer-rule { position: absolute; left: 112px; top: 237px; width: 977px; height: 1px; background: #555; }
  .legal { position: absolute; top: 258px; font-size: 12.5px; color: var(--white); white-space: nowrap; }
  .legal-sep { position: absolute; left: 908px; top: 250px; width: 1px; height: 24px; background: #aaa; }
</style>
</head>
<body>

<section class="section hero">
  <div class="brand"><span class="brand-dot"></span>Lotrafy</div>
  <nav class="main-nav">
    <a href="#" style="left:337px">Home</a>
    <a href="#" style="left:422px">About</a>
    <a href="#" style="left:512px">How TI Work</a>
    <a href="#" style="left:657px">Offers</a>
    <a href="#" style="left:751px">Contacts</a>
  </nav>
  <h1 class="heading hero-title">Welcome to Lotrafy</h1>
  <p class="hero-sub">The Future of MetaVerse Casinos Awaits. Invest Now, and Share the Wins Tomorrow!</p>
  <a class="btn" href="#">Get Started</a>
  <div class="hero-art" role="img" aria-label="Casino scene with roulette wheel, playing cards, dice and chips"></div>
</section>

<section class="section why">
  <div class="why-art" role="img" aria-label="Glowing playing cards with swirling golden light"></div>
  <h2 class="heading why-title">Why MetaVerse Casino?</h2>
  <p class="why-text">Picture a world where traditional casino gaming meets the innovation of the MetaVerse. That's what Lotrafy.io is bringing to the table. A seamlessly integrated experience where online betting enters a limitless digital realm, expanding with boundless possibilities. From blackjack tables set amidst virtual jungles to roulette nestled within mountain terrains, the MetaVerse Casino doesn't just offer games - it offers experiences.</p>
</section>

<section class="section how">
  <h2 class="heading how-title">How It Works</h2>
  <p class="how-text">We need a bankroll to set the wheels in motion. The strength of our casino lies in its foundational capital. Crowdfunding is our key, leveraging the dynamic world of cryptocurrency. Lock-in periods ensure you enjoy sustained returns. Investments will be locked for a specific duration (e.g., 2 years), during which you earn monthly from the casino's operations. Your Return is linked directly to the casino's performance. The better we do, the higher your earnings. Early Withdrawals come with fines, incentivizing longer participation and bigger rewards. Investment cuts fuel the casino's operations, funding marketing and operational costs. Profit sharing maximizes investor returns. Up to 70% of the casino's profits are distributed among the stakeholders. Investment Rounds: More Than Just Money</p>

  <div class="round-card first" style="left:112px">
    <div class="round-badge"><span class="label">ROUND</span><span class="num">1</span></div>
    <p class="round-text">Secure the bankroll. Launch our innovative Chatwave casino.</p>
    <a class="btn" href="#">Read More</a>
  </div>
  <div class="round-card" style="left:444px">
    <div class="round-badge"><span class="label">ROUND</span><span class="num">2</span></div>
    <p class="round-text">Bring the MetaVerse to life. Dive into the limitless expanses, owning shops, designing venues.</p>
    <a class="btn" href="#">Read More</a>
  </div>
  <div class="round-card" style="left:776px">
    <div class="round-badge"><span class="label">ROUND</span><span class="num">3</span></div>
    <p class="round-text">Expand horizons. From web versions of the casino to introducing leveraged trading.</p>
    <a class="btn" href="#">Read More</a>
  </div>
</section>

<section class="section human">
  <div class="human-art" role="img" aria-label="Golden aces, dice, chips and roulette wheel in dark sparkling light"></div>
  <h2 class="heading human-title">The Human Touch</h2>

  <div class="feature" style="top:180px">
    <h3><svg width="12" height="12" viewBox="0 0 12 12"><path d="M1 1l4 5-4 5M6 1l4 5-4 5" fill="none" stroke="#ff1f5a" stroke-width="1.8"/></svg>Robust IT Infrastructure</h3>
    <p>Our commitment is unyielding security and flawless user experience.</p>
  </div>
  <div class="feature" style="top:301px">
    <h3><svg width="12" height="12" viewBox="0 0 12 12"><path d="M1 1l4 5-4 5M6 1l4 5-4 5" fill="none" stroke="#ff1f5a" stroke-width="1.8"/></svg>Effective Liquidity Management</h3>
    <p>With a balance of hot and cold wallets, and real-time metric assessments, we're always ahead of the game.</p>
  </div>
  <div class="feature" style="top:423px">
    <h3><svg width="12" height="12" viewBox="0 0 12 12"><path d="M1 1l4 5-4 5M6 1l4 5-4 5" fill="none" stroke="#ff1f5a" stroke-width="1.8"/></svg>Expert Operational Oversight</h3>
    <p>A dedicated team ensures seamless casino operations.</p>
  </div>
  <div class="feature" style="top:514px">
    <h3><svg width="12" height="12" viewBox="0 0 12 12"><path d="M1 1l4 5-4 5M6 1l4 5-4 5" fill="none" stroke="#ff1f5a" stroke-width="1.8"/></svg>Conclusion</h3>
    <p>The Dice is Cast</p>
  </div>
</section>

<section class="section future">
  <h2 class="heading future-title">The Future Is Now</h2>
  <p class="future-text">The MetaVerse beckons. A world of limitless possibilities, unparalleled gaming experiences, and lucrative returns is just around the corner. With Lotrafy.io, you're not just investing in a project; you're investing in a revolution. The question isn't if you should join but how much you should contribute. Step into the future, and let's share the wins!</p>
</section>

<footer class="section footer">
  <div class="brand"><span class="brand-dot"></span>Lotrafy</div>
  <div class="socials"><span></span><span></span><span></span><span></span><span></span><span></span></div>
  <div class="newsletter-label">Subscribe Our Newsletter</div>
  <div class="email-field">Email Address</div>
  <div class="subscribe-btn">Subscribe Here</div>
  <nav class="footer-nav">
    <a href="#" style="left:112px">Home</a>
    <a href="#" style="left:195px">About</a>
    <a href="#" style="left:285px">How TI Work</a>
    <a href="#" style="left:430px">Offers</a>
    <a href="#" style="left:523px">Contacts</a>
  </nav>
  <div class="footer-rule"></div>
  <div class="legal" style="left:112px">© 2023 All Rights Reserved</div>
  <div class="legal" style="left:772px">Terms &amp; Conditions</div>
  <div class="legal-sep"></div>
  <div class="legal" style="left:929px">privacy policy</div>
</footer>

</body>
</html>
```